Redesign Project: Adobe Captivate Math Activity

Hello, I am looking for an excellent graphic designer who understands E-Learning and can help redesign a few activities from a user interface and user experience perspective. Basically make it look less 90s style and clunky.

This is like a test for a larger project, where we have 500+ pages that need redesign. I'm trying to find talented freelancers who are willing to do the redesign directly on Adobe Captivate. You would likely need to learn a bit about the tool if you don't already have that experience if interested in the larger project.

Redesign this page (using any tool you want) and the best one will earn a chance at the larger project ($5,000 USD)

```html
<!DOCTYPE html>
<html lang="en">
<head>
<meta charset="utf-8">
<title>Bear Equation Activity</title>
<link rel="stylesheet" href="https://fonts.googleapis.com/css2?family=Open+Sans:wght@400;600;700&display=swap">
<style>
  :root {
    --page-bg: #ffffff;
    --frame-line: #cbbbe4;
    --header-bg: #e8e8ea;
    --ink: #1f1f24;
    --accent-purple: #7a4ea8;
    --bear-cyan: #3fc6ef;
    --bear-cyan-light: #8fe0f8;
    --bear-red: #e5323c;
    --bear-red-light: #f47d84;
    --bear-purple: #9b63ca;
    --bear-purple-light: #c7a2e6;
    --bear-green: #22a548;
    --bear-green-light: #6fd28c;
    --plus-blue: #4fc2ee;
    --tile-line: #d4d4d8;
    --tile-foot: #dcdcde;
    --reader-top: #f0c6bd;
    --reader-bottom: #e0646c;
  }
  * { box-sizing: border-box; margin: 0; padding: 0; }
  html, body { width: 1200px; height: 794px; overflow: hidden; background: var(--page-bg); }
  body { position: relative; font-family: "Open Sans", Arial, sans-serif; color: var(--ink); }

  .activity-frame {
    position: absolute; left: 29px; top: 10px; width: 1144px; height: 768px;
    border: 2px solid var(--frame-line); border-radius: 8px;
    background: linear-gradient(to bottom, #ffffff 82%, #f5f4f8 100%);
    box-shadow: 0 4px 18px rgba(122, 78, 168, 0.08);
  }
  .problem-bar {
    position: absolute; left: 33px; top: 14px; width: 1136px; height: 84px;
    background: var(--header-bg); border-radius: 6px 6px 0 0;
  }
  .problem-title {
    position: absolute; left: 16px; top: 18px;
    font-size: 27px; font-weight: 400; color: var(--ink);
  }
  .reader-icon {
    position: absolute; right: 12px; top: 18px; width: 38px; height: 46px;
    border-radius: 10px;
    background: linear-gradient(var(--reader-top), var(--reader-bottom));
  }

  .instruction {
    position: absolute; left: 62px; top: 157px;
    font-size: 15px; font-weight: 600; color: var(--ink);
  }
  .equation-label {
    position: absolute; left: 842px; top: 139px; width: 120px; height: 62px;
    border: 2px solid var(--accent-purple); border-radius: 4px;
    display: flex; align-items: center; justify-content: center;
    font-size: 20px; font-weight: 600; color: var(--ink);
  }

  .bear {
    position: absolute; width: 68px; height: 84px;
    border-radius: 46% 46% 38% 38% / 42% 42% 40% 40%;
    box-shadow: inset 0 -6px 0 rgba(0, 0, 0, 0.10);
  }
  .bear--cyan   { background: radial-gradient(circle at 35% 28%, var(--bear-cyan-light), var(--bear-cyan) 62%); }
  .bear--red    { background: radial-gradient(circle at 35% 28%, var(--bear-red-light), var(--bear-red) 62%); }
  .bear--purple { background: radial-gradient(circle at 35% 28%, var(--bear-purple-light), var(--bear-purple) 62%); }
  .bear--green  { background: radial-gradient(circle at 35% 28%, var(--bear-green-light), var(--bear-green) 62%); }

  .bear-tray .bear { left: 555px; }
  .bear-tray .bear--cyan   { top: 218px; }
  .bear-tray .bear--red    { top: 306px; }
  .bear-tray .bear--purple { top: 398px; }
  .bear-tray .bear--green  { top: 494px; }

  .answer-tile {
    position: absolute; width: 93px; height: 110px;
    border: 1px solid var(--tile-line); background: #fff;
    border-bottom: 12px solid var(--tile-foot);
  }
  .answer-tile .bear { left: 12px; top: 7px; }

  .row-one .answer-tile { top: 268px; }
  .row-two .answer-tile { top: 446px; }
  .tile-first  { left: 716px; }
  .tile-second { left: 865px; }
  .tile-result { left: 1010px; }

  .operator { position: absolute; }
  .plus-sign   { left: 817px; }
  .equals-sign { left: 966px; }
  .row-one .plus-sign   { top: 302px; }
  .row-one .equals-sign { top: 313px; }
  .row-two .plus-sign   { top: 480px; }
  .row-two .equals-sign { top: 491px; }

  .reset-button {
    position: absolute; left: 1045px; top: 708px; width: 108px; height: 40px;
    border: 2px solid var(--accent-purple); border-radius: 20px; background: #fff;
    font-family: "Open Sans", Arial, sans-serif; font-size: 16px; font-weight: 700;
    color: var(--accent-purple); letter-spacing: 0.5px;
  }
</style>
</head>
<body>
  <div class="activity-frame"></div>

  <header class="problem-bar">
    <h1 class="problem-title">Type or Paste Problem Here</h1>
    <div class="reader-icon" role="img" aria-label="Small child reading a book"></div>
  </header>

  <p class="instruction">Drag and drop the bears below to help you solve the problem.</p>
  <div class="equation-label">Equation</div>

  <div class="bear-tray">
    <div class="bear bear--cyan" role="img" aria-label="Blue counting bear"></div>
    <div class="bear bear--red" role="img" aria-label="Red counting bear"></div>
    <div class="bear bear--purple" role="img" aria-label="Purple counting bear"></div>
    <div class="bear bear--green" role="img" aria-label="Green counting bear"></div>
  </div>

  <div class="equation-row row-one">
    <div class="answer-tile tile-first">
      <div class="bear bear--cyan" role="img" aria-label="Blue counting bear"></div>
    </div>
    <svg class="operator plus-sign" width="44" height="44" viewBox="0 0 44 44" aria-label="plus">
      <rect x="15" y="0" width="14" height="44" rx="3" fill="var(--plus-blue)"/>
      <rect x="0" y="15" width="44" height="14" rx="3" fill="var(--plus-blue)"/>
    </svg>
    <div class="answer-tile tile-second">
      <div class="bear bear--red" role="img" aria-label="Red counting bear"></div>
    </div>
    <svg class="operator equals-sign" width="26" height="22" viewBox="0 0 26 22" aria-label="equals">
      <rect x="0" y="0" width="26" height="6" fill="var(--ink)"/>
      <rect x="0" y="15" width="26" height="6" fill="var(--ink)"/>
    </svg>
    <div class="answer-tile tile-result">
      <div class="bear bear--purple" role="img" aria-label="Purple counting bear"></div>
    </div>
  </div>

  <div class="equation-row row-two">
    <div class="answer-tile tile-first">
      <div class="bear bear--purple" role="img" aria-label="Purple counting bear"></div>
    </div>
    <svg class="operator plus-sign" width="44" height="44" viewBox="0 0 44 44" aria-label="plus">
      <rect x="15" y="0" width="14" height="44" rx="3" fill="var(--plus-blue)"/>
      <rect x="0" y="15" width="44" height="14" rx="3" fill="var(--plus-blue)"/>
    </svg>
    <div class="answer-tile tile-second">
      <div class="bear bear--cyan" role="img" aria-label="Blue counting bear"></div>
    </div>
    <svg class="operator equals-sign" width="26" height="22" viewBox="0 0 26 22" aria-label="equals">
      <rect x="0" y="0" width="26" height="6" fill="var(--ink)"/>
      <rect x="0" y="15" width="26" height="6" fill="var(--ink)"/>
    </svg>
    <div class="answer-tile tile-result">
      <div class="bear bear--green" role="img" aria-label="Green counting bear"></div>
    </div>
  </div>

  <button class="reset-button" type="button">RESET</button>
</body>
</html>
```